Web Design for online C2C site

We need a web design for a brand new website that has users logging into an account and uploading pictures of goods and services that they want to trade.
We like 'fresh' and simple websites that have a white background, with easy navigation, a splash of colour (grey, blue, and green is a colour scheme that appeals to us) but doesn't look overly boring.
The site needs a modern look for an old type of trade - a barter system.
We have attached a file with our logo and would like to use the top logo from the file (grey, green, and blue)
Updates
Project Deadline Extended
Reason: The timeline has been extended until this Sunday, December 2nd for all who require extra time to design a web layout.
Cheers,
Margot
Industry/Entity Type
Trade
Look and feel
Each slider illustrates characteristics of the customer's brand and the style your logo design should communicate.

```html
<!DOCTYPE html>
<html lang="en">
<head>
<meta charset="utf-8">
<title>Barterly – List, Swap, Match</title>
<link rel="stylesheet" href="https://fonts.googleapis.com/css2?family=Source+Sans+3:wght@300;400;600;700&family=Arimo:wght@400&family=Indie+Flower&display=swap">
<style>
  :root {
    --ink: #2f2f2f;
    --ink-soft: #444444;
    --hand: #4a4a4a;
    --muted: #a9a9a9;
    --nav-grey: #6d6d6d;
    --brand-green: #4cb817;
    --brand-blue: #7a8fd6;
    --header-fade: #efefef;
    --footer-bg: #f0f0f0;
    --rule: #c9c9c9;
    --field-bg: #f5f5f5;
    --field-border: #d6d6d6;
    --ring: #ececec;
    --social: #5f86b8;
    --white: #ffffff;
  }
  * { box-sizing: border-box; margin: 0; padding: 0; }
  html, body { width: 1200px; height: 918px; overflow: hidden; background: var(--white); }
  body { position: relative; font-family: "Source Sans 3", sans-serif; color: var(--ink); }

  .site-header {
    position: absolute; left: 0; top: 0; width: 1200px; height: 172px;
    background: linear-gradient(to bottom, var(--white) 0%, var(--header-fade) 100%);
  }
  .brand { position: absolute; left: 137px; top: 27px; display: flex; align-items: center; gap: 12px; }
  .brand-mark { width: 96px; height: 96px; border-radius: 50%; background: var(--brand-blue); }
  .brand-name { font-size: 60px; font-weight: 600; color: var(--brand-blue); letter-spacing: -1px; line-height: 1; }

  .account-links { position: absolute; right: 159px; top: 20px; font-size: 13px; color: var(--ink); }
  .account-links span { margin: 0 5px; }
  .login-form .field {
    position: absolute; top: 63px; width: 145px; height: 25px;
    background: var(--field-bg); border: 1px solid var(--field-border);
    font: 12px "Source Sans 3", sans-serif; color: var(--muted); padding: 4px 6px;
  }
  .field-user { left: 730px; }
  .field-pass { left: 897px; }
  .forgot { position: absolute; right: 226px; top: 103px; font-size: 13px; color: var(--ink); }
  .login-btn {
    position: absolute; left: 984px; top: 99px; width: 58px; height: 21px;
    background: var(--brand-green); color: var(--white); font-size: 13px;
    text-align: center; line-height: 21px;
  }

  .main-nav {
    position: absolute; left: 210px; top: 156px; width: 761px; height: 36px;
    background: var(--nav-grey); border-radius: 9px;
  }
  .main-nav a {
    position: absolute; top: 0; line-height: 34px; font-size: 19px; font-weight: 300;
    color: var(--white); text-decoration: none; transform: translateX(-50%);
  }
  .main-nav .sep { position: absolute; top: 11px; width: 1px; height: 17px; background: #e6e6e6; }

  .hero-circle {
    position: absolute; border-radius: 50%; background: var(--ring);
    box-shadow: 0 0 4px rgba(0,0,0,0.08);
  }
  .hero-circle .photo { position: absolute; inset: 11px; border-radius: 50%; }
  .circle-list { left: 343px; top: 307px; width: 226px; height: 226px; }
  .circle-list .photo {
    background:
      linear-gradient(to top, rgba(70,70,70,0.55) 0%, rgba(70,70,70,0) 22%),
      linear-gradient(100deg, #d8b98c 0%, #e9d6bb 30%, #f3eee8 55%, #fafafa 100%);
  }
  .circle-match { left: 506px; top: 430px; width: 226px; height: 226px; }
  .circle-match .photo {
    background:
      linear-gradient(to top, #f2f2f2 0%, #e6e6e6 22%, rgba(230,230,230,0) 34%),
      linear-gradient(to bottom, #cfc6bd 0%, #c9a88a 40%, #b98f6e 65%, #8c6d57 100%);
  }
  .circle-swap { left: 539px; top: 260px; width: 226px; height: 226px; }
  .circle-swap .photo {
    background:
      linear-gradient(to top, #d9a85f 0%, #e2bb7e 24%, rgba(226,187,126,0) 40%),
      linear-gradient(90deg, rgba(0,0,0,0) 60%, rgba(236,140,60,0.45) 80%, rgba(0,0,0,0) 95%),
      linear-gradient(to bottom, #efefef 0%, #e4ddd3 35%, #c79f78 60%, #a9845f 100%);
  }

  .step-label { position: absolute; font-family: "Indie Flower", cursive; font-size: 40px; line-height: 1; color: var(--hand); }
  .label-list { left: 313px; top: 243px; }
  .label-swap { left: 812px; top: 312px; }
  .label-match { left: 337px; top: 562px; }
  .step-arrows { position: absolute; left: 0; top: 0; }

  .site-footer {
    position: absolute; left: 0; top: 712px; width: 1200px; height: 172px;
    background: var(--footer-bg); border-top: 1px solid #dedede;
  }
  .footer-col { position: absolute; top: 14px; }
  .footer-col h3 { font-size: 14px; font-weight: 600; color: var(--ink); margin-bottom: 8px; }
  .footer-col ul { list-style: none; font-family: "Arimo", sans-serif; font-size: 11px; color: var(--ink-soft); }
  .footer-col li { height: 18px; }
  .footer-rule { position: absolute; top: 14px; width: 1px; height: 122px; background: var(--rule); }
  .social { display: flex; gap: 6px; }
  .social span { width: 16px; height: 16px; background: var(--social); }

  .copyright {
    position: absolute; left: 0; top: 895px; width: 1200px; text-align: center;
    font-family: "Arimo", sans-serif; font-size: 11px; color: var(--ink);
  }
</style>
</head>
<body>
  <header class="site-header">
    <div class="brand">
      <div class="brand-mark"></div>
      <div class="brand-name">Barterly</div>
    </div>
    <div class="account-links">Login<span>|</span>Register</div>
    <div class="login-form">
      <div class="field field-user">Username</div>
      <div class="field field-pass">Password</div>
      <div class="forgot">Forgot your username?</div>
      <div class="login-btn">Login</div>
    </div>
  </header>

  <nav class="main-nav">
    <a style="left:77px">Home</a>
    <span class="sep" style="left:147px"></span>
    <a style="left:224px">About</a>
    <span class="sep" style="left:297px"></span>
    <a style="left:371px">Browse</a>
    <span class="sep" style="left:436px"></span>
    <a style="left:515px">Services</a>
    <span class="sep" style="left:600px"></span>
    <a style="left:677px">Contact</a>
  </nav>

  <main class="hero">
    <div class="hero-circle circle-list"><div class="photo" role="img" aria-label="Photo of a smiling woman listing goods on a laptop"></div></div>
    <div class="hero-circle circle-match"><div class="photo" role="img" aria-label="Photo of children browsing matches together on a computer screen"></div></div>
    <div class="hero-circle circle-swap"><div class="photo" role="img" aria-label="Photo of two girls swapping food across a lunch table"></div></div>

    <div class="step-label label-list">List</div>
    <div class="step-label label-swap">Swap</div>
    <div class="step-label label-match">Match</div>

    <svg class="step-arrows" width="1200" height="918" fill="none" stroke="#1e1e1e" stroke-width="2.2" stroke-linecap="round">
      <path d="M389 273 Q420 282 442 302"/>
      <path d="M430 300 L442 303 L438 291"/>
      <path d="M858 352 Q865 385 825 380 Q800 376 789 352"/>
      <path d="M786 364 L788 351 L799 356"/>
      <path d="M427 607 Q440 630 498 593"/>
      <path d="M486 592 L499 592 L495 604"/>
    </svg>
  </main>

  <footer class="site-footer">
    <div class="footer-col" style="left:178px">
      <h3>Who We Are</h3>
      <ul><li>About Us</li><li>Sitemap</li><li>Website Terms</li><li>Terms of Business</li><li>Privacy Policy</li></ul>
    </div>
    <span class="footer-rule" style="left:306px"></span>
    <div class="footer-col" style="left:362px">
      <h3>Community</h3>
      <ul><li>Business Websites</li><li>Reviews</li><li>Quick Tour</li><li>Pricing</li><li>Free Trial</li></ul>
    </div>
    <span class="footer-rule" style="left:497px"></span>
    <div class="footer-col" style="left:546px">
      <h3>Event</h3>
      <ul><li>Marketing Tips</li><li>Search Optimisation</li><li>Social Media</li><li>Video Marketing</li><li>Business Cases</li></ul>
    </div>
    <span class="footer-rule" style="left:704px"></span>
    <div class="footer-col" style="left:744px">
      <h3>Services</h3>
      <ul><li>Help/Contact us</li><li>Business directory</li><li>Legal notices</li><li>Privacy policy</li><li>Terms &amp; Conditions</li></ul>
    </div>
    <span class="footer-rule" style="left:885px"></span>
    <div class="footer-col" style="left:917px">
      <h3>Follow us</h3>
      <div class="social"><span></span><span></span><span></span><span></span></div>
    </div>
  </footer>

  <p class="copyright">Copyright © 2012 Barterly Company. All rights reserved.</p>
</body>
</html>
```